I need a business card.

I need a simple, minimalist, business card. I think the coolest business card I have ever seen is Marty Vexler's from Brimstone Heist... it is just a little creepy for the real world.
I am a photographer and I need a card that I can give to brides or potential portrait customers that is simple and classy.
My name is Gil Anstrade. My website is www.gilanstrade-example.com
Please design my card.
I think it could be as simple as my name, phone # and website... where the rest of my contact could be found... or maybe my email and no website... I am open to ideas. I imagined the card on thick card stock with a black background...

```html
<!DOCTYPE html>
<html lang="en">
<head>
<meta charset="utf-8">
<title>Gil Anstrade Photography – Business Card</title>
<link rel="stylesheet" href="https://fonts.googleapis.com/css2?family=Arimo:wght@700&display=swap">
<style>
  :root {
    --backdrop: #a8a8a8;
    --card: #ffffff;
    --rule: #000000;
    --lettering: #ffffff;
    --glow: rgba(0, 0, 0, 0.75);
  }
  * { margin: 0; padding: 0; box-sizing: border-box; }
  html, body {
    width: 1200px;
    height: 1200px;
    overflow: hidden;
    background: var(--backdrop);
  }
  .canvas {
    position: relative;
    width: 1200px;
    height: 1200px;
    background: var(--backdrop);
    font-family: "Arimo", Arial, sans-serif;
    font-weight: 700;
  }
  .card {
    position: absolute;
    left: 198px;
    width: 772px;
    height: 486px;
    background: var(--card);
  }
  .card--front { top: 66px; }
  .card--back { top: 618px; }
  .rule {
    position: absolute;
    left: 0;
    width: 100%;
    height: 5px;
    background: var(--rule);
  }
  .glow-text {
    position: absolute;
    color: var(--lettering);
    text-shadow: 0 0 4px var(--glow), 0 0 8px var(--glow), 2px 3px 6px var(--glow);
    white-space: nowrap;
    line-height: 1;
  }
  .brand-name {
    left: 0;
    width: 100%;
    top: 189px;
    text-align: center;
    font-size: 64px;
    letter-spacing: 7px;
  }
  .brand-tagline {
    right: 50px;
    top: 262px;
    font-size: 19px;
    letter-spacing: 3px;
  }
  .contact-web {
    left: 0;
    width: 100%;
    top: 139px;
    text-align: center;
    font-size: 32px;
    letter-spacing: 2.5px;
  }
  .contact-phone {
    left: 0;
    width: 100%;
    top: 298px;
    text-align: center;
    font-size: 34px;
    letter-spacing: 4px;
    word-spacing: 8px;
  }
</style>
</head>
<body>
<main class="canvas">
  <section class="card card--front" aria-label="Card front">
    <div class="rule" style="top:178px"></div>
    <h1 class="glow-text brand-name">GIL ANSTRADE</h1>
    <p class="glow-text brand-tagline">PHOTOGRAPHY</p>
    <div class="rule" style="top:291px"></div>
  </section>

  <section class="card card--back" aria-label="Card back">
    <div class="rule" style="top:128px"></div>
    <p class="glow-text contact-web">www.gilanstrade-example.com</p>
    <div class="rule" style="top:184px"></div>
    <div class="rule" style="top:282px"></div>
    <p class="glow-text contact-phone">555 014 2387</p>
    <div class="rule" style="top:344px"></div>
  </section>
</main>
</body>
</html>
```